Quorbeline.com.au - Managed online product sales programs, software platform and apps.

1. Sales & Distribution.We sell your products. On multiple websites, or to major retailers and independents, Clearance and job lots. We managed sales of products via our existing retail channels or a combination of .our channels and clients channels.
2. Software Applications. Use our platforms to manage the products, sales, tracking , customer service and more. Download our apps. Use of our platforms, like www.vaklur.com , or one of our many webstores, like shopnovari.com.au . Use of our apps for product management, sales, tracking and customer service notifications
3. Marketing .Omni channel Programs Online Marketing and SEO optimisation, to maximise your exposure. Marketing - SEO and strategies to increase sales and broaden exposure.

4. Consulting. Special projects and Custom work from advise, to software development. Consulting and Review - Specialised and customised work and business intelligence to improve clients business systems.

Target Market(s)

Target customers are either:
Wholesalers, i.e. companies who own warehouses of inventory and distribute products as wholesalers.
Retailers, i.e. companies operating multiple retail stores and now want to start an online sales program.
Dropship agents, i.e. people who act as brokers, selling products on behalf of wholesalers.
Freight and transport companies who need realtime tracking of products, during delivery from pickup aat warehouse through to delicery at customer.

Industry/Entity Type

Software

Colors

Designer to choose colors to be used in the design.

Requirements
Must have
• A. Simple home page without clutter. Just an easy registration and startup.
minimal menus.
B. Use of icons to indicate each of the 4 areas of work. Namely:
1. Sales - managed sales of products via our existing retail channels or a combination of .our channels and clients channels.
2. Software - use of our platforms, like www.vaklur.com , or one of our many webstores. Use of our apps for product management, sales, tracking and customer service notifications
3. Marketing - SEO and strategies to increase sales and broaden exposure.
4. Consulting and Review - Specialised and customised work and business intelligence to improve clients business systems.

C. Registration wizard to on-board a supplier in 3 easy steps, and start selling products. For example list on Trondlo in 2 easy steps.

D. Use of HTML5 for graphic interface, moving icons and images for a dynamic experience.

E. Internal app-store to download our own apps.

F. Graphical explanations instead of words.

G. Real images and photos
Should not have
• Many menus.
long winded wordy explanations.

```html
<!DOCTYPE html>
<html lang="en">
<head>
<meta charset="utf-8">
<title>Quorbeline – Managed Sales, Software &amp; Marketing</title>
<link href="https://fonts.googleapis.com/css2?family=Open+Sans:wght@400;600;700;800&display=swap" rel="stylesheet">
<style>
:root{
  --pink:#e4489a;
  --ink:#222;
  --text:#666;
  --muted:#888;
  --nav:#555;
  --hero-bg:#f1f0ec;
  --form-bg:#d9d4ca;
  --wizard-bg:#f4f4f4;
  --footer-bg:#e1e1e1;
  --grey-btn:#6a6a6a;
  --arrow:#a9a9a9;
  --sales-tone:#e6e1d6;
  --software-tone:#72c0a9;
  --marketing-tone:#6fa3c4;
  --consulting-tone:#c7e9df;
  --partner:#3d5a9e;
}
*{box-sizing:border-box;margin:0;padding:0}
html,body{width:1150px;height:1200px;overflow:hidden;background:#fff;font-family:"Open Sans",Arial,sans-serif}
.page{position:relative;width:1150px;height:1200px}
.abs{position:absolute}

/* header */
.brand{left:100px;top:30px;font-size:32px;font-weight:800;color:var(--ink);letter-spacing:1px;line-height:44px}
.brand-mark{display:inline-block;width:14px;height:14px;background:var(--pink);margin-left:8px;vertical-align:middle}
.nav a{position:absolute;top:47px;font-size:13px;color:var(--nav);text-decoration:none;letter-spacing:.3px}
.nav a.active{color:var(--pink)}
.btn-small{top:41px;height:29px;line-height:29px;font-size:13px;color:#fff;text-align:center;border-radius:2px}
.btn-register{left:916px;width:77px;background:var(--pink)}
.btn-login{left:997px;width:57px;background:var(--grey-btn)}

/* hero */
.hero{left:0;top:102px;width:1150px;height:439px;background:var(--hero-bg)}
.hero-photo{left:0;top:0;width:650px;height:439px;background:linear-gradient(90deg,#ece9e4 0%,#e7e2dc 15%,#d9cfc6 35%,#cdbfb3 50%,#e6e1db 80%,var(--hero-bg) 100%)}
.hero-title{left:584px;top:48px;font-size:32px;color:var(--pink);font-weight:400;white-space:nowrap}
.hero-copy{left:586px;top:96px;width:412px;font-size:13px;line-height:22px;color:var(--text)}
.signup{left:585px;top:200px;width:411px;height:179px;background:var(--form-bg);border-radius:2px}
.field{position:absolute;width:175px;height:38px;background:#fff;border-radius:2px;font-size:13px;color:var(--text);padding:0 14px;line-height:38px}
.btn-start{position:absolute;left:261px;top:124px;width:123px;height:37px;background:var(--pink);color:#fff;font-size:15px;line-height:37px;text-align:center;border-radius:2px;letter-spacing:.3px}
.slide-arrow{top:201px}

/* services */
.service{top:583px;width:260px;text-align:center}
.service-icon{display:block;width:128px;height:128px;border-radius:50%;margin:0 auto}
.service h2{margin-top:18px;font-size:21px;line-height:28px;font-weight:400;color:var(--pink);white-space:nowrap}
.service p{font-size:13px;line-height:20px;color:var(--muted);margin-top:4px}
.partner-name{font-size:24px;font-weight:600;color:var(--partner);margin-top:6px;line-height:34px}
.tag-badge{left:840px;top:772px;width:62px;height:52px;background:#4a4a4a;border-radius:4px;transform:rotate(-12deg)}
.tag-copy{left:912px;top:770px;width:128px;text-align:center;font-size:13px;line-height:20px;color:var(--muted)}

/* wizard */
.wizard{left:95px;top:890px;width:960px;height:163px;background:var(--wizard-bg)}
.wizard h3{position:absolute;top:28px;width:100%;text-align:center;font-size:22px;font-weight:400;color:var(--pink)}
.step{position:absolute;top:88px;font-size:18px;line-height:22px;color:var(--nav)}

/* footer */
.footer{left:0;top:1091px;width:1150px;height:109px;background:var(--footer-bg)}
.footer-links{position:absolute;left:96px;top:29px;font-size:13px;color:#333;word-spacing:1px}
.footer-links span{margin:0 9px}
.copyright{position:absolute;left:96px;top:59px;font-size:13px;color:#333;word-spacing:2px}
.social{position:absolute;right:96px;top:45px;font-size:12px;color:#555;word-spacing:6px}
</style>
</head>
<body>
<div class="page">

  <header>
    <div class="abs brand">QUORBELINE<span class="brand-mark"></span></div>
    <nav class="nav">
      <a class="active" style="left:423px" href="#">HOME</a>
      <a style="left:503px" href="#">ABOUT US</a>
      <a style="left:608px" href="#">SERVICE</a>
      <a style="left:699px" href="#">PRODUCTS</a>
      <a style="left:808px" href="#">CONTACT US</a>
    </nav>
    <div class="abs btn-small btn-register">REGISTER</div>
    <div class="abs btn-small btn-login">LOGIN</div>
  </header>

  <section class="abs hero">
    <div class="abs hero-photo" role="img" aria-label="Photo of a smiling businesswoman in a dark blazer holding a tablet, soft bright office background"></div>
    <svg class="abs slide-arrow" style="left:20px" width="35" height="35" viewBox="0 0 35 35"><circle cx="17.5" cy="17.5" r="17.5" fill="var(--arrow)"/><path d="M20 10 L13 17.5 L20 25" stroke="#fff" stroke-width="4" fill="none" stroke-linecap="round"/></svg>
    <svg class="abs slide-arrow" style="left:1095px" width="35" height="35" viewBox="0 0 35 35"><circle cx="17.5" cy="17.5" r="17.5" fill="var(--arrow)"/><path d="M15 10 L22 17.5 L15 25" stroke="#fff" stroke-width="4" fill="none" stroke-linecap="round"/></svg>
    <h1 class="abs hero-title">Interdum malesuada fames</h1>
    <p class="abs hero-copy">Phasellus euismod diam a dignissim commodo. Nam mattis pretium ante, vel hendrerit nisi rhoncus eu. Donec vel augue posuere, facilisis dolor ut, porta purus. Etiam rhoncus purus massa, sed ornare nisi gravida quis.</p>
    <form class="abs signup">
      <div class="field" style="left:19px;top:18px">Name</div>
      <div class="field" style="left:209px;top:18px">E-mail</div>
      <div class="field" style="left:19px;top:72px">Password</div>
      <div class="field" style="left:209px;top:72px">Confirm Password</div>
      <div class="btn-start">GET STARTED</div>
    </form>
  </section>

  <section>
    <div class="abs service" style="left:66px">
      <div class="service-icon" style="background:var(--sales-tone)" role="img" aria-label="Sales illustration: shopping basket"></div>
      <h2>SALES</h2>
      <p>Managed sales of products via<br>our existing retail channels or a<br>combination of .our channels<br>and clients channels</p>
    </div>
    <div class="abs service" style="left:311px">
      <div class="service-icon" style="background:var(--software-tone)" role="img" aria-label="Software illustration: settings gear"></div>
      <h2>SOFTWARE</h2>
      <p>Pellentesque habitant morbi</p>
      <div class="partner-name">vaklur.com</div>
    </div>
    <div class="abs service" style="left:549px">
      <div class="service-icon" style="background:var(--marketing-tone)" role="img" aria-label="Marketing illustration: megaphone"></div>
      <h2>MARKETING</h2>
      <p>Managed sales of products via<br>our existing retail channels or a<br>combination of .our channels<br>and clients channels</p>
    </div>
    <div class="abs service" style="left:799px">
      <div class="service-icon" style="background:var(--consulting-tone)" role="img" aria-label="Consulting and review illustration: quotation marks"></div>
      <h2>CONSULTING &amp; REVIEW</h2>
    </div>
    <div class="abs tag-badge" role="img" aria-label="Partner webstore badge"></div>
    <p class="abs tag-copy">Proin quis enim sit<br>amet dolor consect<br>etur varius nec</p>
  </section>

  <section class="abs wizard">
    <h3>REGISTRATION WIZARD</h3>
    <svg class="abs" style="left:61px;top:98px" width="30" height="30" viewBox="0 0 30 30"><rect width="30" height="30" rx="2" fill="#555"/><path d="M8 22 L10 16 L20 6 L24 10 L14 20 Z" fill="none" stroke="#fff" stroke-width="1.8"/></svg>
    <div class="step" style="left:103px">ENTER YOUR<br>DETAILS</div>
    <svg class="abs" style="left:278px;top:96px" width="36" height="36" viewBox="0 0 36 36"><circle cx="18" cy="18" r="16.5" fill="none" stroke="#c8c8c8" stroke-width="2.5"/><path d="M9 18 H25 M19 12 L25 18 L19 24" fill="none" stroke="#c8c8c8" stroke-width="2.5"/></svg>
    <svg class="abs" style="left:386px;top:92px" width="30" height="32" viewBox="0 0 30 32"><g fill="#555"><circle cx="4" cy="4" r="3.5"/><circle cx="4" cy="12" r="3.5"/><circle cx="4" cy="20" r="3.5"/><circle cx="4" cy="28" r="3.5"/><rect x="11" y="2" width="19" height="4"/><rect x="11" y="10" width="19" height="4"/><rect x="11" y="18" width="19" height="4"/><rect x="11" y="26" width="19" height="4"/></g></svg>
    <div class="step" style="left:427px">CHOOSE SERVICE<br>YOU WANT</div>
    <svg class="abs" style="left:639px;top:96px" width="36" height="36" viewBox="0 0 36 36"><circle cx="18" cy="18" r="16.5" fill="none" stroke="#c8c8c8" stroke-width="2.5"/><path d="M9 18 H25 M19 12 L25 18 L19 24" fill="none" stroke="#c8c8c8" stroke-width="2.5"/></svg>
    <svg class="abs" style="left:743px;top:95px" width="32" height="32" viewBox="0 0 32 32"><rect width="32" height="32" rx="2" fill="#555"/><path d="M10 16 L14 21 L22 10" fill="none" stroke="#fff" stroke-width="2"/></svg>
    <div class="step" style="left:785px">GET STARTED<br>NOW</div>
  </section>

  <footer class="abs footer">
    <div class="footer-links">Home<span>|</span>About us<span>|</span>Service<span>|</span>Products<span>|</span>Contact us</div>
    <div class="copyright">Copyright © 2014 Quorbeline. All rights reserved</div>
    <div class="social">Fenlobo Chirpwell</div>
  </footer>

</div>
</body>
</html>
```